A reimagined website for a cross-border tax firm

There are two aspects to this project for Brindlemoor Tax Advisory:
1) I need a logo update to accommodate increasing focus and specialization in my business. The byline under the name “Brindlemoor Tax Advisory” needs to change:
ORIGINAL: TAX SUPPORT FOR PUBLIC ACCOUNTING FIRMS
REVISED: CROSS-BORDER TAX SERVICES • U.S. & CANADA
2) I need a website “refresh” (see current website at www.levyhelpdesk.example) based on this logo – a new vision for a website with greater clarity, focus and organization. It should represent a re-envisioning of the current approach, and not the wholesale abandonment of the style represented there. I need it to be creative, compelling and attention grabbing, but still professional. This should, at a minimum, update any places where the old name/logo is used, but I want the redesign to go beyond this to something more intuitive. I need high quality separate PNG files of the various logo styles for use in various documents, but HTML coding would be a helpful but not necessary addition.

Target Market(s)

People in need of cross-border tax services - Canada and US

Coding

Number of Pages Required

Requirements
Must have
• Greater crispness, sharpness - higher resolution
• A more compelling, organized approach - make the wording and images more accessible to the website user (especially the staff bios, which have scroll bars now)
Nice to have
• Replacement of stock image with a true image of the Halifax skyline
Should not have
• Deviate from colour pattern represented in website logo of blue/orange
• Deviate from existing logo except for word replacement

```html
<!DOCTYPE html>
<html lang="en">
<head>
<meta charset="utf-8">
<title>Brindlemoor Tax Advisory</title>
<link href="https://fonts.googleapis.com/css2?family=Lora:wght@400;700&family=Roboto:wght@400;500;700&display=swap" rel="stylesheet">
<style>
:root{
  --bg:#121212;
  --bg-2:#1f1f1f;
  --orange:#f6a21c;
  --orange-deep:#e8891a;
  --gold:#e6b22e;
  --navy:#1c3e6d;
  --sky:#1c8fd6;
  --icon-blue:#1f7fc9;
  --panel:#2a2a2a;
  --text:#ffffff;
  --muted:#d4d8de;
  --rule:#3a3a3a;
}
*{box-sizing:border-box;margin:0;padding:0}
html,body{width:842px;height:1200px;overflow:hidden}
body{
  position:relative;
  background:radial-gradient(ellipse at 50% 40%,var(--bg-2),var(--bg) 75%);
  font-family:"Roboto",Arial,sans-serif;color:var(--text);
}
.abs{position:absolute}

/* brand name placeholder */
.brand{position:absolute;width:180px;text-align:center}
.brand-line{display:flex;align-items:center;justify-content:center;gap:6px}
.brand-square{width:9px;height:9px;background:var(--orange);flex:none}
.brand-name{font-family:"Roboto",Arial,sans-serif;font-size:11.5px;font-weight:500;color:var(--text);text-transform:uppercase;white-space:nowrap}
.brand-byline{font-family:"Roboto",Arial,sans-serif;font-size:6.4px;font-weight:400;color:var(--muted);margin-top:6px;white-space:nowrap}
.header-brand{left:87px;top:60px}
.footer-brand{left:93px;top:1052px}

/* header */
.call{left:607px;top:25px}
.call-icon{position:absolute;left:0;top:0;width:24px;height:24px;background:var(--orange);display:flex;align-items:center;justify-content:center}
.call-label{position:absolute;left:36px;top:-2px;font-size:8.5px;font-weight:500;white-space:nowrap}
.call-number{position:absolute;left:35px;top:9px;font-size:16px;font-weight:700;color:var(--orange);white-space:nowrap}
.nav-rule{left:305px;top:69px;width:447px;height:1px;background:var(--orange-deep)}
.nav{left:306px;top:70px;height:35px;display:flex;list-style:none}
.nav li{font-size:8.6px;font-weight:500;padding:0 8px;line-height:35px;white-space:nowrap}
.nav li.active{background:var(--orange);color:#1a1a1a}

/* hero */
.hero{left:0;top:105px;width:842px;height:348px;background:linear-gradient(180deg,#5c7fa8 0%,#9db4cc 30%,#b8a890 46%,#33587f 56%,#1f4d7e 75%,#163c66 100%)}
.hero-title{left:0;top:336px;width:842px;text-align:center;font-family:"Lora",Georgia,serif;font-size:29px;font-weight:700}
.hero-btn{left:373px;top:390px;width:97px;height:27px;background:var(--orange);color:#b3261e;font-size:10px;font-weight:700;display:flex;align-items:center;justify-content:center;gap:5px}
.hero-arrow{top:255px;width:23px;height:35px;background:rgba(255,255,255,.85);display:flex;align-items:center;justify-content:center}

/* service panels */
.panel{top:478px;height:210px}
.panel-individuals{left:91px;width:332px;background:var(--navy)}
.panel-firms{left:423px;width:328px;background:var(--sky)}
.panel h2{position:absolute;top:26px;font-family:"Lora",Georgia,serif;font-size:14.5px;font-weight:700}
.panel p{position:absolute;top:53px;width:180px;font-size:7.8px;line-height:14px;text-align:justify;color:#e8eef6}
.panel .btn{position:absolute;top:167px;height:16px;padding:0 7px;background:var(--orange);color:#3a2400;font-size:7.6px;font-weight:700;line-height:16px}

/* team */
.team{left:91px;top:688px;width:660px;height:272px;background:var(--panel);border:1px solid #444}
.team h2{position:absolute;top:30px;width:100%;text-align:center;font-family:"Lora",Georgia,serif;font-size:14px;font-weight:700}
.member{position:absolute;top:81px;width:141px;text-align:center}
.member-photo{width:141px;height:141px;background:linear-gradient(180deg,#3e3e3e,#262626)}
.member-name{margin-top:13px;font-family:"Lora",Georgia,serif;font-size:8.6px;font-weight:700;color:var(--gold);white-space:nowrap}

/* footer */
.footer-col h3{font-family:"Lora",Georgia,serif;font-size:7px;font-weight:400;letter-spacing:.4px}
.footer-menu{left:313px;top:1004px}
.footer-menu ul{list-style:none;margin-top:14px}
.footer-menu li{font-size:8px;line-height:12.4px;color:#e4e4e4}
.footer-follow{left:463px;top:1004px}
.social{display:flex;gap:6px;margin-top:12px}
.social span{width:20px;height:20px;border-radius:50%}
.footer-contact{left:587px;top:1004px;width:170px}
.contact-row{position:absolute;left:8px;font-size:8px;line-height:12.4px;color:#e4e4e4;display:flex;gap:12px;white-space:nowrap}
.footer-rule{left:91px;top:1139px;width:660px;height:1px;background:var(--rule)}
.copyright{left:0;top:1160px;width:842px;text-align:center;font-size:8px;color:#ddd}
</style>
</head>
<body>

<header>
  <div class="brand header-brand">
    <div class="brand-line"><span class="brand-square"></span><span class="brand-name">Brindlemoor Tax Advisory</span></div>
    <div class="brand-byline">CROSS-BORDER TAX SERVICES • U.S. &amp; CANADA</div>
  </div>

  <div class="abs call">
    <div class="call-icon">
      <svg width="14" height="14" viewBox="0 0 24 24"><path fill="#1a1a1a" d="M6.6 10.8a15 15 0 0 0 6.6 6.6l2.2-2.2a1 1 0 0 1 1-.25 11.4 11.4 0 0 0 3.6.57 1 1 0 0 1 1 1V20a1 1 0 0 1-1 1A17 17 0 0 1 3 4a1 1 0 0 1 1-1h3.5a1 1 0 0 1 1 1c0 1.25.2 2.45.57 3.57a1 1 0 0 1-.25 1z"/></svg>
    </div>
    <div class="call-label">CALL US NOW</div>
    <div class="call-number">(555) 014-2290</div>
  </div>

  <div class="abs nav-rule"></div>
  <ul class="abs nav">
    <li class="active">HOME</li>
    <li>OUR TEAM</li>
    <li>FOR INDIVIDUALS</li>
    <li>FOR PUBLIC ACCOUNTING FIRMS</li>
    <li>CONTACT</li>
    <li>PAYMENT</li>
  </ul>
</header>

<section>
  <div class="abs hero" role="img" aria-label="Photograph of a city harbour skyline at dusk over calm blue water"></div>
  <div class="abs hero-arrow" style="left:0">
    <svg width="8" height="12" viewBox="0 0 8 12"><path d="M6 1L1 6l5 5" stroke="#333" stroke-width="1.5" fill="none"/></svg>
  </div>
  <div class="abs hero-arrow" style="left:819px">
    <svg width="8" height="12" viewBox="0 0 8 12"><path d="M2 1l5 5-5 5" stroke="#333" stroke-width="1.5" fill="none"/></svg>
  </div>
  <h1 class="abs hero-title">Tax Services</h1>
  <div class="abs hero-btn">READ MORE
    <svg width="5" height="7" viewBox="0 0 5 7"><path d="M0 0l5 3.5L0 7z" fill="#b3261e"/></svg>
  </div>
</section>

<section>
  <div class="abs panel panel-individuals">
    <svg class="abs" style="left:34px;top:32px" width="40" height="82" viewBox="0 0 40 82">
      <circle cx="20" cy="8" r="8" fill="var(--icon-blue)"/>
      <path d="M10 18h20l9 20-6 6-3-6v40h-6V52h-2v26h-6V38l-3 6-6-6z" fill="var(--icon-blue)"/>
    </svg>
    <h2 style="left:110px">Individuals</h2>
    <p style="left:110px">If you are an individual in need of tax support, we may be able to help you. Our services are designed to complement those offered by your existing accountant – we aim to work alongside your existing advisor(s) during those times when the complexity of your situation demands specialized advice.</p>
    <div class="btn" style="left:112px">READ MORE</div>
  </div>

  <div class="abs panel panel-firms">
    <svg class="abs" style="left:38px;top:28px" width="58" height="58" viewBox="0 0 58 58">
      <g fill="var(--navy)">
        <rect x="0" y="0" width="27" height="27" rx="3"/>
        <rect x="31" y="0" width="27" height="27" rx="3"/>
        <rect x="0" y="31" width="27" height="27" rx="3"/>
        <rect x="31" y="31" width="27" height="27" rx="3"/>
      </g>
      <g stroke="var(--sky)" stroke-width="3" stroke-linecap="round">
        <path d="M13.5 6v15M6 13.5h15M38 13.5h13M8 38l11 11M19 38L8 49M38 44.5h13"/>
      </g>
      <circle cx="44.5" cy="38.5" r="2" fill="var(--sky)"/>
      <circle cx="44.5" cy="50.5" r="2" fill="var(--sky)"/>
    </svg>
    <h2 style="left:122px">Public Accounting Firms</h2>
    <p style="left:122px">In general, our PAF clients are small firms which are not large enough to have their own internal tax specialists. We can assist you as you compete with larger PAFs, by providing you with access to tax assistance on an "as-needed" basis.</p>
    <div class="btn" style="left:124px">READ MORE</div>
  </div>
</section>

<section class="abs team">
  <h2>OUR TEAM</h2>
  <div class="member" style="left:73px">
    <div class="member-photo" role="img" aria-label="Portrait photo of a team member in a dark suit"></div>
    <div class="member-name">Martin R. Colvey, CPA, CGA, EA</div>
  </div>
  <div class="member" style="left:270px">
    <div class="member-photo" role="img" aria-label="Portrait photo of a team member in a dark suit"></div>
    <div class="member-name">Declan Hartwell, CPA, CA</div>
  </div>
  <div class="member" style="left:459px">
    <div class="member-photo" role="img" aria-label="Portrait photo of a team member in a white blouse"></div>
    <div class="member-name">Nora E. Colvey</div>
  </div>
</section>

<footer>
  <div class="brand footer-brand">
    <div class="brand-line"><span class="brand-square"></span><span class="brand-name">Brindlemoor Tax Advisory</span></div>
    <div class="brand-byline">CROSS-BORDER TAX SERVICES • U.S. &amp; CANADA</div>
  </div>

  <div class="abs footer-col footer-menu">
    <h3>MENU</h3>
    <ul>
      <li>Home</li>
      <li>Our Team</li>
      <li>For Individuals</li>
      <li>For Public Accounting Firms</li>
      <li>Contact</li>
      <li>Payment</li>
    </ul>
  </div>

  <div class="abs footer-col footer-follow">
    <h3>FOLLOW US</h3>
    <div class="social">
      <span style="background:#3b5a9a"></span>
      <span style="background:#1da1f2"></span>
      <span style="background:#3f51b5"></span>
    </div>
  </div>

  <div class="abs footer-col footer-contact">
    <h3>CONTACT US</h3>
    <div class="contact-row" style="top:28px">
      <svg width="7" height="10" viewBox="0 0 10 14" style="margin-top:3px"><path d="M5 0a5 5 0 0 0-5 5c0 4 5 9 5 9s5-5 5-9a5 5 0 0 0-5-5zm0 7a2 2 0 1 1 0-4 2 2 0 0 1 0 4z" fill="#fff"/></svg>
      <span>418 Quarrystone Lane, Unit 7<br>Port Avalen, Nova Scotia&nbsp; B0X 2K5</span>
    </div>
    <div class="contact-row" style="top:64px">
      <svg width="8" height="8" viewBox="0 0 24 24" style="margin-top:2px"><path fill="#fff" d="M6.6 10.8a15 15 0 0 0 6.6 6.6l2.2-2.2a1 1 0 0 1 1-.25 11.4 11.4 0 0 0 3.6.57 1 1 0 0 1 1 1V20a1 1 0 0 1-1 1A17 17 0 0 1 3 4a1 1 0 0 1 1-1h3.5a1 1 0 0 1 1 1c0 1.25.2 2.45.57 3.570a1 1 0 0 1-.25 1z"/></svg>
      <span>(555) 014-2290</span>
    </div>
  </div>

  <div class="abs footer-rule"></div>
  <div class="abs copyright">Copyright © 2017 Brindlemoor Tax Advisory Inc.</div>
</footer>

</body>
</html>
```